Dora Finch's Contemporary HOMEVEST Business Cards

I'd like a dark (almost black or black) background with some white lettering and some in a soft orange shade taken from the flowers. Print my photo large with all the lettering on the side opposite my photo. I'd like a simple, contemporary design similar to one I saw on your site. (All black with a tiny white line border inset from the edges. Glossy coating, please.

Target Market(s)

Real estate clients

Industry/Entity Type

Business

Contact Information for Business Card

medium weight cards

Font styles to use
Other font styles liked:
• Arial and perhaps Dora in script above printed name

Requirements
Must have
• Dora L. Finch
• CRS, GRI, ABR, SRES, e-PRO, CNE
• HOMEVEST Circle of Honor, Gold Key Agent
• HOMEVEST Career Excellence Award
• HOMEVEST Summit - Boulder
• 303 555-0142 . 303 555-0187 cell
• Dora@DoraFinchhomes.example
• ** Attached is the logo for the front of my business card. Please use the red one for HOMEVEST SUMMIT. Let me know if you need it in a different file type.
• On back of card please use this quote:
• “We have worked with Dora Finch on six real estate deals. Dora is prompt, efficient, always does what she says she’s going to do, and she keeps the process moving without being pushy. She’s unbelievably organized and never misses a detail. After having dealt with many hundreds of professional people in our lives, Dora stands out as one of the purely effective. Dora is one of those wonderful people who is not only kind and empathetic, but strong. She’s a great listener. We trust her as an advisor. Dora’s a smart lady who knows real estate—and this town—inside and out. Needless to say, we would work with Dora Finch again in an instant.
• ----- Carl Hudgens
Nice to have
• several creative ideas
• probably should remove dark circle sculpture in background if it shows
• maybe Dora in my script handwriting (orange)
Should not have
• don't know about this field

```html
<!DOCTYPE html>
<html lang="en">
<head>
<meta charset="utf-8">
<title>Dora L. Finch – HOMEVEST Business Card</title>
<link rel="stylesheet" href="https://fonts.googleapis.com/css2?family=Arimo&family=Pinyon+Script&display=swap">
<style>
  :root {
    --backdrop: #5f8799;
    --card-black: #151515;
    --ink-white: #f4f4f4;
    --rule-white: #cfcfcf;
    --flower-orange: #d98d42;
    --photo-warm: #8a7262;
    --photo-deep: #2f2b27;
  }
  * { margin: 0; padding: 0; box-sizing: border-box; }
  html, body { width: 1200px; height: 900px; overflow: hidden; }
  body { background: var(--backdrop); position: relative; font-family: "Arimo", Arial, sans-serif; }

  .card { position: absolute; width: 356px; height: 606px; overflow: hidden; }
  .card-front { left: 239px; top: 91px; }
  .card-back { left: 634px; top: 210px; background: var(--card-black); color: var(--ink-white); text-align: center; }

  .portrait {
    position: absolute; inset: 0;
    background: linear-gradient(180deg, #b9aea4 0%, var(--photo-warm) 35%, #4a413a 65%, var(--photo-deep) 100%);
  }
  .front-signature {
    position: absolute; left: 0; right: 0; top: 548px;
    display: flex; align-items: center; justify-content: center; gap: 14px;
    color: var(--ink-white); font-family: "Pinyon Script", cursive; font-size: 28px;
  }
  .front-signature .rule { width: 48px; height: 1px; background: var(--ink-white); }

  .back-name {
    position: absolute; left: 0; right: 0; top: 118px;
    font-family: "Pinyon Script", cursive; font-size: 42px; color: var(--flower-orange);
  }
  .divider { position: absolute; left: 33px; width: 296px; height: 1px; background: var(--rule-white); }
  .divider-top { top: 226px; }
  .divider-bottom { top: 368px; }
  .credentials {
    position: absolute; left: 0; right: 0; top: 257px;
    font-size: 15.5px; line-height: 21px;
  }
  .contact {
    position: absolute; left: 0; right: 0; top: 423px;
    font-size: 19px; line-height: 25px;
  }
</style>
</head>
<body>
  <section class="card card-front">
    <div class="portrait" role="img" aria-label="Portrait photo of Dora L. Finch seated at a kitchen counter beside orange roses"></div>
    <div class="front-signature">
      <span class="rule"></span><span class="signature-name">Dora L. Finch</span><span class="rule"></span>
    </div>
  </section>

  <section class="card card-back">
    <h1 class="back-name">Dora L. Finch</h1>
    <div class="divider divider-top"></div>
    <p class="credentials">
      CRS, GRI, ABR, SRES, e-PRO, CNE<br>
      HOMEVEST Circle of Honor, Gold Key Agent<br>
      HOMEVEST Career Excellence Award<br>
      HOMEVEST Summit - Boulder
    </p>
    <div class="divider divider-bottom"></div>
    <p class="contact">
      303 555-0142 . 303 555-0187 cell<br>
      Dora@DoraFinchhomes.example
    </p>
  </section>
</body>
</html>
```